依頼詳細
PC版のTOPページと下層1ページ(採用情報)のデザイン制作をお願いいたします。
サイトマップ、依頼内容詳細.txtをご確認いただき、動画のテイストを参考にシンプルで見やすいデザインで制作いただきたいです。
スムーズな連絡と軽微な修正にご対応いただける方へご依頼をさせていただきたいです。
ターゲットは木材資材・建築資材・家具建具資材などを必要とする建築会社様、家具・建具製造会社様などです。
ページ数
2ページ
希望イメージ
シンプル 複雑
単色 カラフル
暗い 明るい
日常 高級
遊び心 厳粛
未来的 伝統的
女性的 男性的
希望する色
茶系、緑系、グレー系
納品ファイル
• イラストレーター形式 (.ai)
補足説明
納品ファイルはXDも可です。
添付してあるアニメーションにテイストを合わせ、
木の温かみを感じさせるデザインで制作してください。
コーポレートですが、あまり堅くなり過ぎないようにしたいです。
BtoB向けの会社ではありますが、就職などを考えている若い方が見ても、
面白そうな企業だなという印象も与えたいです。
動画ダウンロードURLを新たに添付いたしましたので
そちらからダウンロードをお願い致します。
■ 選んだ理由

爽やかな緑を使ったデザインが良かったです。

■ 提案者全員のお礼・コメント

たくさんのご提案をいただきありがとうございました。

```html
<!DOCTYPE html>
<html lang="ja">
<head>
<meta charset="utf-8">
<title>採用情報 | 緑ヶ丘木材株式会社</title>
<link href="https://fonts.googleapis.com/css2?family=Noto+Sans+JP:wght@400;500;700&family=Montserrat:wght@600;700&display=swap" rel="stylesheet">
<style>
:root{
  --green:#5c9a3c;
  --green-soft:#8fb86a;
  --ink:#333333;
  --ink-soft:#666666;
  --line:#cfcfcf;
  --dark:#3a3a3a;
  --band:#eeeeee;
  --white:#ffffff;
}
*{margin:0;padding:0;box-sizing:border-box}
html,body{width:1200px;height:2344px;overflow:hidden}
body{font-family:"Noto Sans JP",sans-serif;color:var(--ink);background:var(--white);position:relative;font-size:14px}
.en{font-family:"Montserrat","Noto Sans JP",sans-serif}

.site-header{position:absolute;top:0;left:0;width:1200px;height:80px;background:var(--white);display:flex;align-items:center;padding-left:40px;z-index:2}
.brand{display:flex;align-items:center;gap:10px;font-size:22px;font-weight:500;color:var(--ink)}
.brand-mark{width:22px;height:22px;background:var(--green-soft)}
.global-nav{display:flex;margin-left:auto;height:80px;align-items:center}
.global-nav a{font-size:13px;font-weight:500;color:var(--ink);text-decoration:none;padding:0 15px}
.global-nav a.current{color:var(--green)}
.nav-contact{background:var(--dark);color:var(--white)!important;height:80px;display:flex;align-items:center;padding:0 30px!important;margin-left:22px}

.hero{position:absolute;top:80px;left:0;width:1200px;height:300px;background:radial-gradient(circle at 25% 40%,#a9cf83 0%,#6fa548 40%,#3f7a2c 100%);display:flex;flex-direction:column;align-items:center;justify-content:center;color:var(--white)}
.hero-title{font-size:54px;font-weight:700;letter-spacing:2px;line-height:1}
.hero-sub{font-size:13px;margin-top:8px}

.lead{position:absolute;top:418px;left:0;width:1200px;text-align:center;font-size:21px;font-weight:700;line-height:1.8}
.lead small{font-size:11px;font-weight:500}

.recruit{position:absolute;top:520px;left:220px;width:760px}
.section-heading{font-size:19px;font-weight:700;padding-bottom:8px;border-bottom:1px solid var(--ink);width:330px}
.recruit-text{margin-top:16px;font-size:14px;line-height:2.1;color:var(--ink-soft)}

.job-table{position:absolute;top:838px;left:220px;width:760px;border-collapse:collapse}
.job-table th,.job-table td{border-bottom:1px solid var(--line);height:52px;text-align:left;font-size:14px}
.job-table th{width:120px;font-weight:700}
.job-table td{color:var(--ink-soft)}
.job-table tr:first-child th,.job-table tr:first-child td{border-top:1px solid var(--line)}

.news{position:absolute;top:1398px;left:0;width:1200px;height:200px;background:var(--band)}
.news-label{position:absolute;top:20px;left:170px;width:290px;height:160px;background:#d9d9d9;padding:28px 30px}
.news-title{font-size:40px;font-weight:700;line-height:1}
.news-sub{font-size:12px;margin-top:6px}
.news-more{position:absolute;left:30px;bottom:24px;width:74px;height:20px;background:var(--white);font-size:10px;display:flex;align-items:center;justify-content:center}
.news-list{position:absolute;top:30px;left:510px;width:560px;list-style:none}
.news-list li{display:flex;align-items:center;height:34px;border-bottom:1px solid var(--line);font-size:12px}
.news-date{width:88px;color:var(--ink-soft)}
.news-tag{width:76px;height:18px;background:var(--white);border:1px solid var(--line);font-size:10px;display:flex;align-items:center;justify-content:center;margin-right:18px}
.news-text{font-weight:500}

.contact{position:absolute;top:1718px;left:0;width:1200px;height:240px;border-top:1px solid var(--line)}
.contact-title{position:absolute;top:50px;left:200px;font-size:48px;font-weight:700;line-height:1}
.contact-sub{position:absolute;top:108px;left:202px;font-size:12px}
.contact-text{position:absolute;top:58px;left:515px;font-size:13px;line-height:2}
.contact-button{position:absolute;top:120px;left:740px;width:260px;height:56px;background:var(--dark);color:var(--white);font-size:13px;display:flex;align-items:center;justify-content:center;gap:10px;text-decoration:none}

.site-footer{position:absolute;top:2040px;left:0;width:1200px;height:276px;border-top:1px solid var(--line)}
.footer-brand{position:absolute;top:46px;left:170px}
.footer-info{position:absolute;top:100px;left:170px;font-size:12px;line-height:1.9;color:var(--ink-soft)}
.footer-tel{position:absolute;top:178px;left:170px;display:flex;align-items:center;gap:10px;font-size:12px}
.footer-tel strong{font-size:22px;font-weight:700;color:var(--ink)}
.sitemap{position:absolute;top:46px;left:620px;display:flex;gap:110px}
.sitemap ul{list-style:none}
.sitemap li{font-size:13px;line-height:2}
.sitemap .sitemap-head{color:var(--green);font-weight:700}
.copyright{position:absolute;top:2316px;left:0;width:1200px;height:28px;background:var(--dark);color:var(--white);font-size:10px;display:flex;align-items:center;justify-content:center}
</style>
</head>
<body>

<header class="site-header">
  <div class="brand"><span class="brand-mark"></span>緑ヶ丘木材株式会社</div>
  <nav class="global-nav">
    <a class="current en" href="#">HOME</a>
    <a href="#">ご挨拶</a>
    <a href="#">会社概要</a>
    <a href="#">事業内容</a>
    <a href="#">取扱商品</a>
    <a href="#">採用情報</a>
    <a class="nav-contact" href="#">お問い合わせ</a>
  </nav>
</header>

<section class="hero" role="img" aria-label="緑の葉を背景に置かれた木製の家の模型の写真">
  <h1 class="hero-title en">RECRUIT</h1>
  <p class="hero-sub">採用情報</p>
</section>

<p class="lead">身近にあふれる木のぬくもりをとどける<br>一緒に木のように成長していける人たちと。<small>(サンプル文です)</small></p>

<section class="recruit">
  <h2 class="section-heading">募集職について</h2>
  <p class="recruit-text">緑ヶ丘木材株式会社では、多種多様な木材をお客様にお届けする营業を担う人達を募集しております。新たな課題の解決や販路の拡大など幅広に挑戦することはもくさんあります。サンプルテキストです。サンプルテキストサンプルテキストサンプルテキストサンプルテキストサンプルテキストサンプルテキストサンプルテキストサンプルテキストサンプルテキストサンプルテキストサンプルテキストサンプルテキスト</p>
</section>

<table class="job-table">
  <tr><th>募集職</th><td>営業職サンプル</td></tr>
  <tr><th>雇用形態</th><td>新卒・中途採用(サンプルテキスト)</td></tr>
  <tr><th>勤務時間</th><td>00：00～00：00（休憩1時間）　週休2日　勤務形態による</td></tr>
  <tr><th>勤務地</th><td>本社（住所）</td></tr>
  <tr><th>給与形態</th><td>月〇〇万円、当社規定により昇給あり</td></tr>
  <tr><th>福利厚生</th><td>社会保険完備、他(サンプルテキスト)</td></tr>
  <tr><th>その他</th><td>(サンプルテキスト)</td></tr>
  <tr><th></th><td>(サンプルテキスト)</td></tr>
</table>

<section class="news">
  <div class="news-label">
    <h2 class="news-title en">NEWS</h2>
    <p class="news-sub">新着情報</p>
    <a class="news-more">一覧 ＞</a>
  </div>
  <ul class="news-list">
    <li><span class="news-date">2021.02.27</span><span class="news-tag">カテゴリ</span><span class="news-text">テキストテキストテキストテキストテキスト</span></li>
    <li><span class="news-date">2021.02.27</span><span class="news-tag">カテゴリ</span><span class="news-text">テキストテキストテキストテキストテキスト</span></li>
    <li><span class="news-date">2021.02.27</span><span class="news-tag">カテゴリ</span><span class="news-text">テキストテキストテキストテキストテキスト</span></li>
    <li><span class="news-date">2021.02.27</span><span class="news-tag">カテゴリ</span><span class="news-text">テキストテキストテキストテキストテキスト</span></li>
  </ul>
</section>

<section class="contact">
  <h2 class="contact-title en">CONTACT</h2>
  <p class="contact-sub">お問い合わせ</p>
  <p class="contact-text">緑ヶ丘木材株式会社へのお問い合わせは下記フォームより<br>お願い致します。</p>
  <a class="contact-button" href="#">お問い合わせフォームへ
    <svg width="14" height="10" viewBox="0 0 14 10"><path d="M0 5h12M8 1l4 4-4 4" stroke="#fff" stroke-width="1.4" fill="none"/></svg>
  </a>
</section>

<footer class="site-footer">
  <div class="brand footer-brand"><span class="brand-mark"></span>緑ヶ丘木材株式会社</div>
  <p class="footer-info">〒000-0000 住所<br>営業時間 08:00-00:00(土日祝は定休日)</p>
  <p class="footer-tel">お電話はお気軽に
    <svg width="18" height="18" viewBox="0 0 24 24"><path d="M6.6 10.8a15 15 0 006.6 6.6l2.2-2.2c.3-.3.7-.4 1-.2 1.1.4 2.3.6 3.6.6.6 0 1 .4 1 1V20c0 .6-.4 1-1 1A17 17 0 013 4c0-.6.4-1 1-1h3.5c.6 0 1 .4 1 1 0 1.3.2 2.5.6 3.6.1.3 0 .7-.2 1z" fill="#333"/></svg>
    <strong class="en">000-000-0000</strong>
  </p>
  <nav class="sitemap">
    <ul>
      <li class="sitemap-head en">SITEMAP</li>
      <li>HOME</li>
      <li>会社概要</li>
      <li>ご挨拶</li>
      <li>事業内容</li>
      <li>採用情報</li>
    </ul>
    <ul>
      <li>取扱商品</li>
      <li>メーカーリンク集</li>
      <li>お問合せ情報</li>
      <li>採用情報</li>
      <li>お問い合わせ</li>
      <li>プライバシーポリシー</li>
    </ul>
  </nav>
</footer>
<p class="copyright">© Copyright 緑ヶ丘木材株式会社. All Right Reserved.</p>

</body>
</html>
```